Banner Ad Design Project for Velmorin watches

I am just launching a new divers watch called the Velmorin Tidewalk Alpha. I require a banner ad for a popular watch website. As my watch is very bright I want it to show this by transitioning from its normal view to a lowlight view where only the luminous hands and hour markers show. you can see the watch at www.velmorin.co.uk to see what i mean.
Updates

Banner ad size is 468x60 pixels size <100Kb in gif or swf

Target Market(s)

luxury watches

Requirements
Must have
• picture of the watch in a slanted view. my company logo. a nice slow transition not jerky cuts

```html
<!DOCTYPE html>
<html lang="en">
<head>
<meta charset="UTF-8">
<title>Velmorin Tidewalk Alpha – Banner Phases</title>
<link href="https://fonts.googleapis.com/css2?family=Tinos&family=Arimo&display=swap" rel="stylesheet">
<style>
  :root {
    --page: #ffffff;
    --banner: #050505;
    --texture-light: #3a3a3a;
    --texture-dark: #0b0b0b;
    --brand-blue: #1a1aff;
    --headline: #f2f2f2;
    --accent-green: #66ff1a;
    --label: #000000;
    --watch-rim: #4a4a4a;
    --watch-face: #e8e8e8;
  }
  * { box-sizing: border-box; margin: 0; padding: 0; }
  html, body {
    width: 1200px;
    height: 900px;
    overflow: hidden;
    background: var(--page);
  }
  .sheet {
    position: relative;
    width: 1200px;
    height: 900px;
  }
  .phase {
    position: absolute;
    left: 128px;
    width: 934px;
  }
  .phase--1 { top: 76px; }
  .phase--2 { top: 232px; }
  .phase--3 { top: 388px; }
  .phase--4 { top: 542px; }
  .phase--5 { top: 698px; }

  .banner {
    position: relative;
    width: 934px;
    height: 120px;
    background: var(--banner);
    overflow: hidden;
  }
  .banner__texture {
    position: absolute;
    left: 0;
    right: 180px;
    bottom: 0;
    height: 92px;
    background:
      linear-gradient(180deg, rgba(5,5,5,1) 0%, rgba(5,5,5,0) 40%),
      linear-gradient(90deg, var(--texture-dark) 0%, var(--texture-light) 45%, var(--texture-dark) 100%);
    opacity: 0.85;
  }
  .banner__watch {
    position: absolute;
    right: 0;
    top: -40px;
    width: 300px;
    height: 210px;
    border-radius: 50%;
    background: radial-gradient(circle at 55% 50%,
      var(--watch-face) 0%, var(--watch-face) 38%,
      var(--watch-rim) 44%, #1c1c1c 60%, var(--banner) 72%);
  }
  .banner__copy {
    position: absolute;
    inset: 0 300px 0 0;
    display: flex;
    align-items: center;
    font-family: "Tinos", "Times New Roman", serif;
    color: var(--headline);
    letter-spacing: 1px;
  }
  .brand-name {
    font-family: "Tinos", "Times New Roman", serif;
    font-size: 60px;
    color: var(--brand-blue);
    margin-left: 30px;
    letter-spacing: 0;
  }
  .tagline {
    font-size: 27px;
    margin-left: 38px;
  }
  .headline {
    font-size: 29px;
    margin-left: 42px;
  }
  .headline--centered { margin-left: 166px; }
  .headline--click { margin-left: 100px; font-size: 31px; }
  .highlight { color: var(--accent-green); margin-left: 10px; }
  .headline__figure { font-size: 42px; margin-left: 6px; }

  .phase__label {
    display: block;
    text-align: center;
    font-family: "Arimo", Arial, sans-serif;
    font-size: 21px;
    color: var(--label);
    margin-top: 6px;
    line-height: 1;
  }
</style>
</head>
<body>
<main class="sheet">

  <section class="phase phase--1">
    <div class="banner">
      <div class="banner__texture" role="img" aria-label="Dark textured background of rounded pebble shapes"></div>
      <div class="banner__watch" role="img" aria-label="Velmorin divers watch shown at a slanted angle in full daylight view"></div>
      <div class="banner__copy">
        <span class="brand-name">Velmorin</span>
        <span class="tagline">DIVERS WATCH</span>
      </div>
    </div>
    <span class="phase__label">PHASE 1</span>
  </section>

  <section class="phase phase--2">
    <div class="banner">
      <div class="banner__texture" role="img" aria-label="Dark textured background of rounded pebble shapes"></div>
      <div class="banner__watch" role="img" aria-label="Velmorin divers watch shown at a slanted angle, light fading"></div>
      <div class="banner__copy">
        <span class="brand-name">Velmorin</span>
        <span class="tagline">DIVERS WATCH</span>
      </div>
    </div>
    <span class="phase__label">PHASE 2</span>
  </section>

  <section class="phase phase--3">
    <div class="banner">
      <div class="banner__texture" role="img" aria-label="Dark textured background of rounded pebble shapes"></div>
      <div class="banner__watch" role="img" aria-label="Velmorin divers watch with luminous hands and hour markers"></div>
      <div class="banner__copy">
        <span class="headline">THE NEW EXCLUSIVE<span class="highlight">TIDEWALK ALPHA</span></span>
      </div>
    </div>
    <span class="phase__label">PHASE 3</span>
  </section>

  <section class="phase phase--4">
    <div class="banner">
      <div class="banner__texture" role="img" aria-label="Dark textured background of rounded pebble shapes"></div>
      <div class="banner__watch" role="img" aria-label="Velmorin divers watch with luminous hands and hour markers"></div>
      <div class="banner__copy">
        <span class="headline headline--centered">LIMITED TO<span class="headline__figure">500</span></span>
      </div>
    </div>
    <span class="phase__label">PHASE 4</span>
  </section>

  <section class="phase phase--5">
    <div class="banner">
      <div class="banner__texture" role="img" aria-label="Dark textured background of rounded pebble shapes"></div>
      <div class="banner__watch" role="img" aria-label="Velmorin divers watch with luminous hands and hour markers"></div>
      <div class="banner__copy">
        <span class="headline headline--click">CLICK HERE FOR DETAILS</span>
      </div>
    </div>
    <span class="phase__label">PHASE 5</span>
  </section>

</main>
</body>
</html>
```